Design the Business card for VaultPeak

Business card required for a professional Cyber Security business.
Company Logo and Icon has already been provided however I would like other options for the logo and icon to compare to. Alternatively, please refine/enhance the image of the logo.icon I have already provided.

If you are going to use the provided logo and icon, I was thinking that the company raised Logo on White background would serve well on the front of the card. See attached. AND, a large company raised stand-alone icon to appear on black background on the back of the card with tagline 'Cyber Risk Management, Governance and Consulting' or 'Cyber Security for your Business' See attached.
Alternatively, provide your own design for the logo and icon.

Target Market(s)

Enterprise, Government, Financial.

Contact Information for Business Card

Teodor Halvik
Founder and CEO

Email Address
Mobile Number
Website URL
LinkedIn URL

Logo Text

VaultPeak - see attached example of logo

Font styles to use
Other font styles liked:
• Berlin Sans FB

Requirements
Must have
• Clean large and bold icon on the back with tagline.
• Horizontal alignment,
Nice to have
• Round edges.
• Raised Logo/Icon
Should not have
• An unprofessional look and feel.

```html
<!DOCTYPE html>
<html lang="en">
<head>
<meta charset="utf-8">
<title>VaultPeak Business Card</title>
<link href="https://fonts.googleapis.com/css2?family=Arimo:wght@400;700&display=swap" rel="stylesheet">
<style>
  :root {
    --page-bg: #e9e6e1;
    --card-black: #000000;
    --card-white: #ffffff;
    --brand-blue: #4472c4;
    --logo-blue: #1f5fae;
    --brand-yellow: #f5b800;
    --text-dark: #333333;
    --text-light: #e6e6e6;
  }
  * { margin: 0; padding: 0; box-sizing: border-box; }
  html, body {
    width: 1200px; height: 900px; overflow: hidden;
    background: var(--page-bg);
    font-family: "Arimo", Arial, sans-serif;
  }
  .stage { position: relative; width: 1200px; height: 900px; }
  .card {
    position: absolute; left: 300px;
    width: 600px; height: 343px;
    border-radius: 10px; overflow: hidden;
    box-shadow: 0 6px 18px rgba(0,0,0,0.18);
  }

  /* Back */
  .card-back { top: 88px; background: var(--card-black); }
  .back-brand {
    position: absolute; top: 110px; left: 0; right: 0;
    display: flex; justify-content: center; align-items: center; gap: 14px;
  }
  .back-brand .brand-dot {
    width: 34px; height: 34px; border-radius: 50%; background: var(--brand-blue);
  }
  .back-brand .brand-name {
    font-weight: 700; font-size: 46px; color: var(--brand-blue);
  }
  .tagline {
    position: absolute; bottom: 62px; left: 0; right: 0; text-align: center;
    color: var(--text-light); font-size: 17px; letter-spacing: 0.2px;
  }

  /* Front */
  .card-front { top: 469px; background: var(--card-white); }
  .person { position: absolute; top: 40px; left: 44px; }
  .person-name { font-weight: 700; font-size: 24px; letter-spacing: 0.5px; }
  .person-name .first { color: var(--brand-blue); }
  .person-name .last { color: var(--brand-yellow); }
  .person-title { font-size: 16px; color: var(--text-dark); margin-top: 4px; }

  .front-brand {
    position: absolute; top: 52px; right: 36px;
    display: flex; align-items: center; gap: 10px;
  }
  .front-brand .brand-dot {
    width: 30px; height: 30px; border-radius: 50%; background: var(--brand-blue);
  }
  .front-brand .brand-name {
    font-weight: 700; font-size: 34px; color: var(--logo-blue);
  }

  .contacts { position: absolute; top: 140px; left: 50px; list-style: none; z-index: 2; }
  .contacts li {
    display: flex; align-items: center; gap: 10px;
    font-size: 17px; color: var(--text-dark); line-height: 24px;
  }
  .contacts svg { width: 14px; height: 14px; flex: none; }

  .wave { position: absolute; left: 0; bottom: 0; width: 600px; height: 200px; }
</style>
</head>
<body>
<main class="stage">

  <section class="card card-back" aria-label="Card back">
    <div class="back-brand">
      <span class="brand-dot"></span>
      <span class="brand-name">VaultPeak</span>
    </div>
    <p class="tagline">Cyber Risk Management, Governance and Consulting</p>
  </section>

  <section class="card card-front" aria-label="Card front">
    <div class="person">
      <h1 class="person-name"><span class="first">TEODOR</span> <span class="last">HALVIK</span></h1>
      <p class="person-title">Founder and CEO</p>
    </div>

    <div class="front-brand">
      <span class="brand-dot"></span>
      <span class="brand-name">VaultPeak</span>
    </div>

    <ul class="contacts">
      <li>
        <svg viewBox="0 0 14 14" aria-hidden="true"><path fill="#f5b800" d="M1 5c0-2 2-3 6-3s6 1 6 3l-2 1-1-2H4L3 6zM3 7h8l1 5H2z"/></svg>
        044-987 654 321
      </li>
      <li>
        <svg viewBox="0 0 14 14" aria-hidden="true"><rect x="1" y="3" width="12" height="8" fill="#f5b800"/><path d="M1 3l6 5 6-5" fill="none" stroke="#fff" stroke-width="1.2"/></svg>
        info@vaultpeak.net
      </li>
      <li>
        <svg viewBox="0 0 14 14" aria-hidden="true"><circle cx="7" cy="7" r="6" fill="#f5b800"/><path d="M1 7h12M7 1c-3 3-3 9 0 12M7 1c3 3 3 9 0 12" fill="none" stroke="#fff" stroke-width="1"/></svg>
        www.vaultpeak.net
      </li>
      <li>
        <svg viewBox="0 0 14 14" aria-hidden="true"><rect x="1" y="1" width="12" height="12" rx="2" fill="#f5b800"/></svg>
        www.profiles.net
      </li>
    </ul>

    <svg class="wave" viewBox="0 0 600 200" preserveAspectRatio="none" aria-hidden="true">
      <path d="M0 128 C 220 122, 380 90, 470 40 C 380 100, 220 134, 0 140 Z" fill="var(--brand-yellow)"/>
      <path d="M0 150 C 220 130, 420 72, 600 25 L 600 200 L 0 200 Z" fill="var(--brand-blue)"/>
      <path d="M0 150 C 220 130, 420 72, 600 25" fill="none" stroke="#fff" stroke-width="4"/>
    </svg>
  </section>

</main>
</body>
</html>
```